QTR

*** Sovan see attached upload **** regarding the changes to the letter THIS IS THE NEW UPLOAD 29/07

Target Market(s)

working people
people looking to borrow $300 - $5000

Requirements
Must have
• open minded
get the Brand out there
not too many words or cluster
Nice to have
• money
people (girl) on it
logo looking vibrant
Should not have
• old style fonts

```html
<!DOCTYPE html>
<html lang="en">
<head>
<meta charset="utf-8">
<title>QTR – Your line of credit</title>
<link rel="stylesheet" href="https://fonts.googleapis.com/css2?family=Quicksand:wght@400;500&family=Parisienne&display=swap">
<style>
  :root {
    --teal: #2fb3b8;
    --sky-top: #2aa6d8;
    --sky-bottom: #0f6fa8;
    --ink: #1d2a33;
    --ink-soft: #333d44;
    --white: #ffffff;
  }
  * { box-sizing: border-box; margin: 0; padding: 0; }
  html, body { width: 854px; height: 1200px; overflow: hidden; background: var(--white); }
  .flyer {
    position: relative; width: 854px; height: 1200px; overflow: hidden;
    font-family: "Quicksand", sans-serif; color: var(--ink);
    background: radial-gradient(circle at 60% 60%, #ffffff 0%, #f3f6f7 100%);
  }

  /* top band */
  .hero { position: absolute; left: 33px; top: 0; width: 819px; height: 480px; display: flex; }
  .hero-questions {
    width: 180px; height: 100%; background: var(--teal); color: var(--white);
    padding: 55px 8px 0 10px; font-size: 19.5px; line-height: 1.25;
  }
  .hero-questions p { margin-bottom: 16px; }
  .hero-panel {
    position: relative; flex: 1; height: 100%;
    background: linear-gradient(160deg, var(--sky-top) 0%, #1a88c0 55%, var(--sky-bottom) 100%);
  }
  .hero-art {
    position: absolute; left: 10px; top: 24px; width: 260px; height: 400px;
    background: radial-gradient(ellipse at 55% 45%, rgba(255,255,255,0.4) 0%, rgba(255,255,255,0.1) 60%, rgba(255,255,255,0) 75%);
  }
  .hero-copy {
    position: absolute; right: 32px; top: 166px; text-align: right;
    color: var(--ink); font-size: 18.5px; line-height: 1.3;
  }
  .hero-copy p { margin-bottom: 12px; }
  .brand-name { font-size: 24px; font-weight: 500; letter-spacing: 1px; display: block; line-height: 1.2; }
  .hero-call {
    position: absolute; right: 32px; bottom: 6px; font-size: 25px; font-weight: 500;
    color: var(--ink); white-space: nowrap;
  }

  /* middle */
  .audience-art {
    position: absolute; left: 55px; top: 512px; width: 354px; height: 270px;
    background: radial-gradient(circle, #e9eef0 0%, #cfd6da 55%, rgba(255,255,255,0) 72%);
  }
  .next-steps { position: absolute; left: 454px; top: 520px; }
  .next-title {
    font-family: "Parisienne", cursive; color: var(--teal); font-size: 31px; font-weight: 400;
    line-height: 1.2; margin-bottom: 2px;
  }
  .next-steps ol { list-style: none; font-size: 22px; line-height: 38px; color: var(--ink-soft); }

  .burst { position: absolute; left: 329px; top: 744px; width: 523px; height: 165px; }
  .burst svg { position: absolute; inset: 0; width: 100%; height: 100%; }
  .burst-text {
    position: absolute; inset: 0; display: flex; flex-direction: column;
    justify-content: center; align-items: center;
    font-family: "Parisienne", cursive; color: var(--white); font-size: 24px; line-height: 1.55;
    padding-top: 20px;
  }

  /* bottom */
  .apply-art {
    position: absolute; left: 49px; top: 842px; width: 281px; height: 213px;
    background: linear-gradient(135deg, #e6e8ea 0%, #d2d6d9 100%); border-radius: 6px;
  }
  .contact { position: absolute; left: 27px; top: 1070px; font-size: 18px; line-height: 31px; color: var(--ink-soft); }
  .contact .phone { font-size: 27px; color: var(--teal); }
  .branches {
    position: absolute; left: 427px; top: 1037px; width: 425px; height: 137px;
    background: var(--teal); color: var(--white); padding: 14px 18px;
    font-size: 18px; line-height: 27px;
  }
</style>
</head>
<body>
<main class="flyer">
  <section class="hero">
    <div class="hero-questions">
      <p>Do u just need<br>$800 for a new<br>phone?</p>
      <p>Or an extra<br>$1000 for the<br>weekend away<br>with the lads?</p>
      <p>Ladies... those<br>shoes or<br>handbag u<br>REALLY need?</p>
      <p>Music festival<br>tixs ??</p>
    </div>
    <div class="hero-panel">
      <div class="hero-art" role="img" aria-label="Shopping trolley overflowing with colourful sale and discount tags"></div>
      <div class="hero-copy">
        <p>Any reason really....<span class="brand-name">QTR</span>is your line of credit</p>
        <p>Pay it off quickly (to get rid of it) and<br>if the need arises again CALL US</p>
        <p>Once you establish your QTR line<br>with us the next loan is easy</p>
        <p>If u fear defaults are holding u back...</p>
      </div>
      <div class="hero-call">call the Girls &amp; have a chat 1300 555 010</div>
    </div>
  </section>

  <div class="audience-art" role="img" aria-label="Ring of small figures with arrows pointing to a red target in the centre"></div>

  <section class="next-steps">
    <h2 class="next-title">What's Next ?</h2>
    <ol>
      <li>1. Apply online</li>
      <li>2. We verify ur stuff</li>
      <li>3. Once APPROVED sign online</li>
    </ol>
  </section>

  <div class="burst">
    <svg viewBox="0 0 500 150" preserveAspectRatio="none" aria-hidden="true">
      <polygon fill="#2fb3b8" points="30,25 50,0 70,25 90,0 110,25 130,0 150,25 170,0 190,25 210,0 230,25 250,0 270,25 290,0 310,25 330,0 350,25 370,0 390,25 410,0 430,25 450,0 470,25 500,45 475,75 500,105 470,125 450,150 430,125 410,150 390,125 370,150 350,125 330,150 310,125 290,150 270,125 250,150 230,125 210,150 190,125 170,150 150,125 130,150 110,125 90,150 70,125 50,150 30,125 0,105 25,75 0,45"/>
    </svg>
    <div class="burst-text">
      <span>Thats it !...Online or Visit a branch</span>
      <span>QTR...YOUR line of credit</span>
    </div>
  </div>

  <div class="apply-art" role="img" aria-label="Simple figure leaning on a speech bubble reading Apply Now"></div>

  <section class="contact">
    <p>Call: <span class="phone">1300 555 020</span></p>
    <p>Online: www.qtrcredit.example</p>
    <p>Email us: hello@qtrcredit.example</p>
  </section>

  <section class="branches">
    <p>Visit a branch:</p>
    <p>Northgate: 12 Harbour Lane Eastfield</p>
    <p>Westbrook: Cnr Birch &amp; Mill Street Parkview<br>Shopping Centre</p>
  </section>
</main>
</body>
</html>
```